Landscape Company Stationary
Biz cards, letterhead, envelopes, etc
Professional
Dean Morvik
P.O. Box 3852
Alder Falls, NJ 07634
foxridgemail@postbrim.com
Dont want address on biz cards, just letterhead and envelopes. Would like to incorporate the stripe and colors that are in our logo.
Logo with colors and fonts to use. Please incorporate the striping too and colors

```html
<!DOCTYPE html>
<html lang="en">
<head>
<meta charset="utf-8">
<title>Foxridge Landscaping Stationery</title>
<link rel="stylesheet" href="https://fonts.googleapis.com/css2?family=Open+Sans:wght@400;700;800&display=swap">
<style>
:root{
  --board:#333;
  --board-edge:#262626;
  --paper:#ffffff;
  --green:#2f8f2f;
  --green-dark:#1d6a1f;
  --green-light:#8cc63f;
  --ink:#444;
  --label:#9a9a9a;
  --faint:#e4efdc;
}
*{box-sizing:border-box;margin:0;padding:0}
html,body{width:1200px;height:408px;overflow:hidden;background:var(--board)}
body{font-family:"Open Sans",Arial,sans-serif;color:var(--ink)}
.board{position:relative;width:1200px;height:408px;background:radial-gradient(ellipse at 50% 40%,#3c3c3c,var(--board-edge))}
.piece{position:absolute;background:var(--paper);overflow:hidden;box-shadow:0 2px 6px rgba(0,0,0,.5)}
.piece svg.wave{position:absolute;left:0;bottom:0;width:100%}
.label{position:absolute;font-size:5px;color:var(--label);text-align:center}
.brand{font-weight:800;color:var(--green);line-height:1;display:flex;align-items:center;gap:3px}
.brand .dot{border-radius:50%;background:var(--green-light);flex:none}
.brand-sub{display:inline-block;background:var(--green);color:#fff;font-weight:700;letter-spacing:.5px}
.contact{font-size:4px;line-height:1.5;color:var(--ink)}
.faint-mark{position:absolute;border-radius:50% 50% 50% 50%/60% 60% 40% 40%;background:radial-gradient(ellipse,var(--faint),rgba(228,239,220,0) 70%)}

/* business cards */
.card{left:96px;width:149px;height:96px}
.card-front{top:36px}
.card-front .brand{position:absolute;left:10px;top:8px;font-size:15px}
.card-front .brand .dot{width:7px;height:7px}
.card-front .brand-sub{position:absolute;left:22px;top:26px;font-size:4px;padding:1px 4px}
.card-front .person{position:absolute;right:10px;top:38px;text-align:right}
.card-front .person .name{font-size:5px;font-weight:700;color:var(--green-dark)}
.card-back{top:156px;height:91px}
.card-back .logo{position:absolute;left:0;right:0;top:24px;display:flex;flex-direction:column;align-items:center;gap:3px}
.card-back .brand{font-size:17px}
.card-back .brand .dot{width:7px;height:7px}
.card-back .brand-sub{font-size:4px;padding:1px 5px}
.card-green{top:271px;height:91px;background:var(--green)}
.card-green .logo{position:absolute;left:0;right:0;top:26px;display:flex;flex-direction:column;align-items:center;gap:3px}
.card-green .brand{font-size:17px;color:#fff}
.card-green .brand .dot{width:7px;height:7px;background:#fff}
.card-green .brand-sub{font-size:4px;padding:1px 5px;background:#fff;color:var(--green)}

/* letterheads */
.letter{top:24px;width:269px;height:365px}
.letter-one{left:264px}
.letter-two{left:552px}
.letter .brand{font-size:19px}
.letter .brand .dot{width:8px;height:8px}
.letter .brand-sub{font-size:4.5px;padding:1px 5px;margin-top:3px}
.letter-one .logo{position:absolute;left:16px;top:14px}
.letter-one .contact{position:absolute;left:122px;top:16px}
.letter-two .logo{position:absolute;left:0;right:0;top:14px;display:flex;flex-direction:column;align-items:center}
.letter .faint-mark{left:70px;top:90px;width:130px;height:170px}
.letter .footer{position:absolute;left:0;right:0;bottom:8px;text-align:center;font-size:4px;color:#fff}

/* envelopes */
.env{width:288px;height:116px}
.env-flap{left:888px;top:29px;background:var(--green-light)}
.env-green{left:888px;top:96px;background:var(--green)}
.env-plain{left:852px;top:168px;height:120px}
.env-front{left:840px;top:240px;height:132px}
.env .flap{position:absolute;left:0;top:0;width:100%;height:100%}
.env .mark{position:absolute;left:50%;top:46px;width:12px;height:12px;margin-left:-6px;border-radius:50%;background:#fff}
.env-flap .mark{background:var(--green-dark)}
.env-front .logo{position:absolute;left:10px;top:10px}
.env-front .brand{font-size:15px}
.env-front .brand .dot{width:6px;height:6px}
.env-front .brand-sub{font-size:4px;padding:1px 4px;margin-top:2px}
.env-front .contact{position:absolute;left:12px;top:44px}
</style>
</head>
<body>
<main class="board">

  <!-- Business card front -->
  <section class="piece card card-front">
    <div class="brand"><span class="dot"></span>Foxridge</div>
    <span class="brand-sub">LANDSCAPING</span>
    <div class="person contact">
      <div class="name">Dean Morvik</div>
      <div>Owner</div>
      <div>Tel (973) 555-0142</div>
      <div>foxridgemail@postbrim.com</div>
    </div>
    <svg class="wave" viewBox="0 0 149 30" height="30" preserveAspectRatio="none">
      <path d="M0 18 C40 4 100 30 149 6 L149 30 L0 30Z" fill="var(--green-light)"/>
      <path d="M0 24 C50 10 100 34 149 14 L149 30 L0 30Z" fill="var(--green)"/>
    </svg>
  </section>
  <div class="label" style="left:96px;top:137px;width:149px">Front Card Option 1</div>

  <!-- Business card back -->
  <section class="piece card card-back">
    <div class="logo">
      <div class="brand"><span class="dot"></span>Foxridge</div>
      <span class="brand-sub">LANDSCAPING</span>
    </div>
    <svg class="wave" viewBox="0 0 149 22" height="22" preserveAspectRatio="none">
      <path d="M0 12 C40 2 100 22 149 4 L149 22 L0 22Z" fill="var(--green-light)"/>
      <path d="M0 16 C50 6 100 24 149 10 L149 22 L0 22Z" fill="var(--green)"/>
    </svg>
  </section>
  <div class="label" style="left:96px;top:252px;width:149px">Back Card Option 1</div>

  <!-- Business card back, green -->
  <section class="piece card card-green">
    <div class="logo">
      <div class="brand"><span class="dot"></span>Foxridge</div>
      <span class="brand-sub">LANDSCAPING</span>
    </div>
  </section>
  <div class="label" style="left:96px;top:367px;width:149px">Back Card Option 2</div>

  <!-- Letterhead one -->
  <section class="piece letter letter-one">
    <div class="logo">
      <div class="brand"><span class="dot"></span>Foxridge</div>
      <span class="brand-sub">LANDSCAPING</span>
    </div>
    <div class="contact">
      <div>Tel (973) 555-0142</div>
      <div>Fax (973) 555-0143</div>
      <div>foxridgemail@postbrim.com</div>
    </div>
    <div class="faint-mark" role="img" aria-label="Faint brand mark area"></div>
    <svg class="wave" viewBox="0 0 269 50" height="50" preserveAspectRatio="none">
      <path d="M0 20 C80 0 180 40 269 8 L269 50 L0 50Z" fill="var(--green-light)"/>
      <path d="M0 28 C90 8 180 48 269 16 L269 50 L0 50Z" fill="var(--green)"/>
    </svg>
    <div class="footer">P.O. Box 3852 · Alder Falls, NJ 07634</div>
  </section>
  <div class="label" style="left:264px;top:392px;width:269px">Letterhead Option 1</div>

  <!-- Letterhead two -->
  <section class="piece letter letter-two">
    <div class="logo">
      <div class="brand"><span class="dot"></span>Foxridge</div>
      <span class="brand-sub">LANDSCAPING</span>
    </div>
    <div class="faint-mark" role="img" aria-label="Faint brand mark area"></div>
    <svg class="wave" viewBox="0 0 269 50" height="50" preserveAspectRatio="none">
      <path d="M0 8 C90 40 190 0 269 22 L269 50 L0 50Z" fill="var(--green-light)"/>
      <path d="M0 16 C90 48 190 8 269 30 L269 50 L0 50Z" fill="var(--green)"/>
    </svg>
    <div class="footer">P.O. Box 3852 · Alder Falls, NJ 07634 · foxridgemail@postbrim.com</div>
  </section>
  <div class="label" style="left:552px;top:392px;width:269px">Letterhead Option 2</div>

  <!-- Envelopes -->
  <section class="piece env env-flap">
    <svg class="flap" viewBox="0 0 288 116" preserveAspectRatio="none">
      <path d="M0 0 H288 V60 L144 96 L0 60Z" fill="var(--paper)"/>
      <path d="M0 0 H288 V40 L144 80 L0 40Z" fill="var(--green)"/>
    </svg>
    <span class="mark"></span>
  </section>

  <section class="piece env env-green">
    <svg class="flap" viewBox="0 0 288 116" preserveAspectRatio="none">
      <path d="M0 0 H288 V44 L144 84 L0 44Z" fill="var(--green-dark)"/>
    </svg>
    <span class="mark"></span>
  </section>

  <section class="piece env env-plain">
    <svg class="flap" viewBox="0 0 288 120" preserveAspectRatio="none">
      <path d="M0 0 H288 V44 L144 86 L0 44Z" fill="#f2f2f2"/>
      <path d="M0 44 L144 86 L288 44" fill="none" stroke="#ddd"/>
    </svg>
  </section>

  <section class="piece env env-front">
    <div class="logo">
      <div class="brand"><span class="dot"></span>Foxridge</div>
      <span class="brand-sub">LANDSCAPING</span>
    </div>
    <div class="contact">
      <div>P.O. Box 3852</div>
      <div>Alder Falls, NJ 07634</div>
    </div>
    <svg class="wave" viewBox="0 0 288 40" height="40" preserveAspectRatio="none">
      <path d="M0 18 C90 0 190 34 288 6 L288 40 L0 40Z" fill="var(--green-light)"/>
      <path d="M0 26 C90 8 190 42 288 14 L288 40 L0 40Z" fill="var(--green)"/>
    </svg>
  </section>
  <div class="label" style="left:840px;top:392px;width:336px">Envelope Options</div>

</main>
</body>
</html>
```